60 Ways to de-stress Poster

I would like a poster ( A4 full colour) with a list of 60 ways to destress. I would like the design to be clean and stylish (not cartoonish)

My Target market is stressed out mums so I want the poster to feel inspirational and relaxing to look at.

I have added a sample of something I like - but open to other ideas

Finished art would be print ready pdf

Target Market(s)

Mums who are stressed out - mainly new mums. I want this to be a poster that someone would happily put up that looks more like artwork.

Requirements
Must have
• My logo elements and colours but happy to incorporate other colours that blend well into it.

Colours:
Bright green: Pantone 376
Bright green as CMYK: c: 45.2% m: 0% y: 100% k: 0%

Logo text large grey: 70% black
Logo text strapline: 75% black
Tree: 80% black

Fonts:
Logo 'Willowbrook Calm': Verdana
Logo 'Counselling & coaching services for mums': Gill Sans Light
Should not have
• No cartoonish images - I want it very clean and stylish

```html
<!DOCTYPE html>
<html lang="en">
<head>
<meta charset="utf-8">
<title>60 Ways to De Stress – Willowbrook Calm</title>
<link rel="stylesheet" href="https://fonts.googleapis.com/css2?family=Josefin+Sans:ital,wght@0,300;0,400;0,600;1,300;1,400;1,600;1,700&family=Quicksand:wght@300;400&display=swap">
<style>
  :root {
    --page: #ffffff;
    --paper: #f1f2f3;
    --green: #8dc63f;
    --teal: #1ea6a4;
    --teal-soft: #7fcdcb;
    --grey-dark: #58595b;
    --grey: #6d6e71;
    --grey-soft: #a7a9ac;
    --tree: #4d4d4f;
  }
  * { margin: 0; padding: 0; box-sizing: border-box; }
  html, body { width: 1200px; height: 1000px; overflow: hidden; background: var(--page); }
  .poster {
    position: absolute; left: 310px; top: 57px;
    width: 628px; height: 886px;
    background: var(--paper);
    font-family: "Josefin Sans", sans-serif;
  }
  .headline-number, .headline-line {
    position: absolute; font-family: "Quicksand", sans-serif; font-weight: 300;
    line-height: 1; white-space: nowrap; letter-spacing: 1px;
  }
  .headline-number { left: 127px; top: 52px; font-size: 138px; color: var(--green); letter-spacing: -6px; }
  .headline-line { left: 290px; font-size: 41px; }
  .headline-line.top { top: 80px; color: var(--green); }
  .headline-line.bottom { top: 121px; color: var(--grey-dark); }

  .tree-illustration { position: absolute; left: 105px; top: 215px; width: 98px; height: 162px; }

  .tip-list { list-style: none; }
  .tip { position: absolute; line-height: 1; white-space: nowrap; font-weight: 300; }
  .tip.vertical { writing-mode: vertical-rl; transform: rotate(180deg); }
  .tip.accent { color: var(--green); font-weight: 700; font-style: italic; }
  .tip.teal { color: var(--teal); font-weight: 400; }
  .tip.teal-soft { color: var(--teal-soft); }
  .tip.grey { color: var(--grey); }
  .tip.grey-soft { color: var(--grey-soft); }
  .tip.italic { font-style: italic; }

  .brand { position: absolute; left: 221px; top: 760px; width: 220px; height: 70px; }
  .brand-name {
    position: absolute; left: 0; top: 35px; font-size: 17px; font-weight: 600;
    color: var(--grey-dark); white-space: nowrap; line-height: 1;
  }
  .brand-strapline {
    position: absolute; left: 0; top: 56px; font-size: 12px; font-weight: 400;
    color: var(--grey-dark); white-space: nowrap; line-height: 1;
  }
  .brand-dot { position: absolute; left: 164px; top: 0; width: 44px; height: 44px; border-radius: 50%; background: var(--tree); }
</style>
</head>
<body>
<main class="poster">
  <h1>
    <span class="headline-number">60</span>
    <span class="headline-line top">WAYS TO</span>
    <span class="headline-line bottom">DE STRESS</span>
  </h1>

  <svg class="tree-illustration" role="img" aria-label="Stylised grey tree with white and green hearts in its crown" viewBox="0 0 98 162">
    <circle cx="49" cy="48" r="48" fill="#6a6b6d"/>
    <rect x="43" y="88" width="14" height="74" fill="#6a6b6d"/>
  </svg>

  <ul class="tip-list">
    <li class="tip teal" style="left:213px;top:214px;font-size:21px">put on some music and dance</li>
    <li class="tip accent" style="left:223px;top:241px;font-size:16px">light a scented candle</li>
    <li class="tip accent" style="left:427px;top:240px;font-size:10px">write a poem</li>
    <li class="tip grey-soft" style="left:215px;top:265px;font-size:15px">take a mini mental holiday</li>
    <li class="tip grey-soft" style="left:428px;top:259px;font-size:12px">fake a smile</li>
    <li class="tip grey-soft" style="left:432px;top:276px;font-size:12px">gaze at the</li>
    <li class="tip grey" style="left:433px;top:290px;font-size:32px">stars</li>
    <li class="tip vertical grey" style="left:400px;top:240px;font-size:18px">make a gratitude list</li>
    <li class="tip teal" style="left:208px;top:285px;font-size:13px;font-weight:600">swing on a swing</li>
    <li class="tip accent" style="left:330px;top:288px;font-size:11px">hug someone</li>
    <li class="tip accent" style="left:181px;top:307px;font-size:10px">go to the park</li>
    <li class="tip grey italic" style="left:268px;top:307px;font-size:9px">take a nap</li>
    <li class="tip vertical accent" style="left:321px;top:308px;font-size:10px">call or visit a friend</li>
    <li class="tip grey-soft" style="left:345px;top:309px;font-size:12px">write in</li>
    <li class="tip grey-soft" style="left:346px;top:325px;font-size:12px">a journal</li>
    <li class="tip teal-soft" style="left:428px;top:321px;font-size:15px">pat a dog</li>
    <li class="tip grey-soft" style="left:172px;top:325px;font-size:18px">listening to music</li>
    <li class="tip grey italic" style="left:200px;top:349px;font-size:12px">buy yourself flowers</li>
    <li class="tip accent" style="left:342px;top:347px;font-size:12px">meditate</li>
    <li class="tip accent" style="left:428px;top:345px;font-size:14px">volunteer</li>
    <li class="tip accent" style="left:428px;top:361px;font-size:14px">your time</li>
    <li class="tip grey-soft italic" style="left:191px;top:369px;font-size:12px">take some deep breaths</li>
    <li class="tip grey" style="left:345px;top:364px;font-size:22px">have</li>
    <li class="tip grey" style="left:345px;top:390px;font-size:15px">a bath</li>
    <li class="tip grey-soft" style="left:428px;top:383px;font-size:12px">make yourself</li>
    <li class="tip grey" style="left:427px;top:399px;font-size:13px">a cup of tea</li>
    <li class="tip accent" style="left:167px;top:385px;font-size:23px;font-style:normal">go for a walk</li>
    <li class="tip vertical teal-soft" style="left:150px;top:383px;font-size:14px">watch the clouds go by</li>
    <li class="tip grey-soft italic" style="left:186px;top:415px;font-size:12px">plant a tree</li>
    <li class="tip grey" style="left:263px;top:413px;font-size:15px">eat something mindfully</li>
    <li class="tip accent" style="left:423px;top:420px;font-size:10px">play in the park</li>
    <li class="tip grey" style="left:187px;top:434px;font-size:15px">paint a picture</li>
    <li class="tip grey-soft" style="left:294px;top:433px;font-size:16px">forgive someone</li>
    <li class="tip grey" style="left:412px;top:434px;font-size:13px">get a massage</li>
    <li class="tip grey-soft" style="left:188px;top:457px;font-size:16px">review your achievements</li>
    <li class="tip grey" style="left:402px;top:454px;font-size:16px">get a haircut</li>
    <li class="tip vertical grey" style="left:171px;top:428px;font-size:9px">stand up and stretch</li>
    <li class="tip vertical accent" style="left:376px;top:453px;font-size:11px">go for a bike ride</li>
    <li class="tip grey-soft" style="left:400px;top:474px;font-size:12px">colour in a picture</li>
    <li class="tip teal" style="left:187px;top:480px;font-size:14px">take a long drive</li>
    <li class="tip grey" style="left:308px;top:476px;font-size:20px">create</li>
    <li class="tip grey" style="left:308px;top:494px;font-size:23px">some</li>
    <li class="tip grey-soft" style="left:308px;top:514px;font-size:14px">routines</li>
    <li class="tip accent" style="left:407px;top:490px;font-size:16px">take a class</li>
    <li class="tip accent" style="left:407px;top:512px;font-size:16px">at the gym</li>
    <li class="tip grey" style="left:187px;top:502px;font-size:19px">read a book</li>
    <li class="tip grey" style="left:147px;top:529px;font-size:16px">play a game</li>
    <li class="tip accent" style="left:251px;top:530px;font-size:14px;font-style:normal">bake some cookies</li>
    <li class="tip grey-soft" style="left:397px;top:532px;font-size:13px">go on a picnic</li>
    <li class="tip grey italic" style="left:149px;top:553px;font-size:12px">perform an act of kindness</li>
    <li class="tip teal-soft" style="left:297px;top:551px;font-size:14px">give yourself a time-out</li>
    <li class="tip accent" style="left:445px;top:551px;font-size:15px">vent</li>
    <li class="tip vertical grey-soft" style="left:487px;top:538px;font-size:15px">watch a funny movie</li>
    <li class="tip grey" style="left:156px;top:573px;font-size:14px">listen to a guided relaxation mp3</li>
    <li class="tip grey" style="left:375px;top:570px;font-size:20px">ask for help</li>
    <li class="tip vertical accent" style="left:145px;top:593px;font-size:13px">de-clutter a drawer</li>
    <li class="tip grey-soft" style="left:163px;top:594px;font-size:19px">disconnect from technology</li>
    <li class="tip accent" style="left:398px;top:597px;font-size:13px">live for today</li>
    <li class="tip accent" style="left:167px;top:620px;font-size:12px">look at a work of art</li>
    <li class="tip grey" style="left:289px;top:616px;font-size:20px">visit a farmers market</li>
    <li class="tip teal-soft" style="left:163px;top:638px;font-size:14px">borrow a book from the library</li>
    <li class="tip accent" style="left:356px;top:640px;font-size:9px">accept what you can't change</li>
    <li class="tip grey-soft" style="left:165px;top:657px;font-size:12px">scale down your to do list</li>
    <li class="tip grey" style="left:303px;top:657px;font-size:14px">write positive self-statements</li>
    <li class="tip grey-soft" style="left:163px;top:676px;font-size:16px">outsource if you can</li>
    <li class="tip accent" style="left:306px;top:677px;font-size:11px">try progressive muscle relaxation</li>
    <li class="tip teal" style="left:165px;top:694px;font-size:30px;font-weight:300">compliment yourself often</li>
  </ul>

  <footer class="brand">
    <span class="brand-dot"></span>
    <span class="brand-name">Willowbrook Calm</span>
    <span class="brand-strapline">counselling &amp; coaching for mums</span>
  </footer>
</main>
</body>
</html>
```